WORK VAN WRAP - Marrowind Floor Coating

I need full-wrap design for my Concrete Coating Business.
Vehicle is: 2019 Vell Stridex 3400 Hi roof cargo van
My business expertise is: Epoxy Floor Coating including Luxuxry Flakes, Luxury Metallics, and Luxury Quartz for outdoor. But the core of my business is in doing the 1-DAY GARAGE FLOOR APPLICATION.
My work is: LifetimeWarranty
My website is not active yet but it will be soon: MARROWINDFLOORCOATING.COM
Phone number: coming soon
Email: coming soon
Colors:
45% black
25% neon green (follow the logo attached)
20% white (for lettering)
10% gray (real picture of a floor attached) feel free about using a better picture
I will attach some pictures of designs I've seen for inspiration purposes only.
Goal: I need the vehicle to stand out among others, a bright green on black that no one can miss with an attractive design that everyone wants to know "what kind of business is that" when they see it parked or driving on the road.

```html
<!DOCTYPE html>
<html lang="en">
<head>
<meta charset="utf-8">
<title>Marrowind Floor Coatings – Van Wrap</title>
<link rel="stylesheet" href="https://fonts.googleapis.com/css2?family=Montserrat:wght@600;700;800&family=Oswald:wght@500;600;700&display=swap">
<style>
  :root {
    --neon: #6fe01f;
    --neon-dark: #4fb310;
    --black: #141414;
    --charcoal: #262626;
    --white: #ffffff;
    --glass: #3a3d40;
    --floor-gray: #9a9c9e;
    --tire: #0c0c0c;
    --rim: #8d9196;
    --page: #ffffff;
  }
  html, body {
    margin: 0;
    padding: 0;
    width: 1200px;
    height: 1200px;
    overflow: hidden;
    background: var(--page);
  }
  .canvas {
    position: relative;
    width: 1200px;
    height: 1200px;
  }
  .van {
    position: absolute;
    left: 0;
    width: 1200px;
    height: 560px;
  }
  .van--side-a { top: 0; }
  .van--side-b { top: 537px; }
  .van svg { position: absolute; inset: 0; }
  .van .label { position: absolute; margin: 0; white-space: nowrap; line-height: 1; }

  .tagline {
    font-family: "Oswald", sans-serif;
    font-weight: 600;
    font-size: 18px;
    letter-spacing: 2px;
    color: var(--neon);
  }
  .tagline .tagline__lead { color: var(--white); }

  .brand-mark {
    position: absolute;
    background: var(--neon);
  }
  .brand-name {
    font-family: "Montserrat", sans-serif;
    font-weight: 800;
    line-height: 1;
  }
  .brand-name--main { font-size: 53px; color: var(--white); }
  .brand-name--sub { font-size: 37px; color: var(--neon); }

  .services {
    font-family: "Oswald", sans-serif;
    font-weight: 500;
    font-size: 13.5px;
    letter-spacing: 0.3px;
  }
  .services--band { color: var(--black); }
  .services--open { color: var(--white); text-align: center; line-height: 1.3 !important; font-size: 13px; }
  .services .divider { color: var(--neon-dark); padding: 0 3px; }
  .services--open .divider { color: var(--neon); }

  .website {
    font-family: "Montserrat", sans-serif;
    font-weight: 700;
    font-size: 16px;
  }
  .website .website__name { color: var(--neon); }
  .website .website__tld { color: var(--white); }
  .website--band .website__name { color: var(--neon-dark); }
  .website--band .website__tld { color: var(--neon-dark); }

  .phone {
    font-family: "Montserrat", sans-serif;
    font-weight: 700;
    font-size: 24px;
    letter-spacing: 1px;
    color: var(--black);
  }

  .seal-text {
    font-family: "Oswald", sans-serif;
    font-weight: 700;
  }
</style>
</head>
<body>
<main class="canvas">

  <!-- Side A: black body with neon front -->
  <section class="van van--side-a" aria-label="Van wrap, version with green front">
    <svg viewBox="0 0 1200 560" width="1200" height="560">
      <defs>
        <clipPath id="body-a">
          <path d="M80,125 Q80,98 112,98 L960,100 Q1008,102 1030,160 L1080,300 Q1140,318 1150,352 L1150,470 Q1150,492 1128,492 L80,495 Q68,495 68,480 Z"/>
        </clipPath>
      </defs>
      <g clip-path="url(#body-a)">
        <rect class="body-black" x="0" y="0" width="1200" height="560" fill="var(--black)"/>
        <rect role="img" aria-label="Gray speckled epoxy floor texture" x="70" y="280" width="640" height="180" fill="var(--charcoal)"/>
        <path class="front-panel" d="M646,90 L1200,90 L1200,560 L770,560 Z" fill="var(--neon)"/>
        <rect class="rocker" x="70" y="440" width="1100" height="60" fill="#0a0a0a"/>
        <path class="front-window" d="M780,190 L920,190 Q945,192 955,240 L962,294 L780,294 Z" fill="var(--glass)"/>
        <rect class="headlight" x="1100" y="345" width="50" height="18" rx="6" fill="#d9dcdf"/>
      </g>
      <rect class="belt-line" x="215" y="302" width="270" height="5" fill="var(--white)"/>
      <rect class="service-band" x="120" y="328" width="605" height="24" fill="var(--white)"/>
      <g class="warranty-seal">
        <circle cx="840" cy="412" r="30" fill="var(--black)"/>
        <circle cx="840" cy="412" r="24" fill="none" stroke="var(--neon)" stroke-width="2"/>
        <rect x="808" y="403" width="64" height="18" fill="var(--white)"/>
        <text class="seal-text" x="840" y="417" text-anchor="middle" font-size="12" fill="var(--black)">LIFETIME</text>
        <text class="seal-text" x="840" y="398" text-anchor="middle" font-size="6.5" fill="var(--white)">WARRANTY</text>
        <text class="seal-text" x="840" y="432" text-anchor="middle" font-size="6.5" fill="var(--white)">WARRANTY</text>
      </g>
      <circle class="wheel" cx="255" cy="500" r="55" fill="var(--tire)"/>
      <circle cx="255" cy="500" r="32" fill="var(--rim)"/>
      <circle class="wheel" cx="990" cy="500" r="55" fill="var(--tire)"/>
      <circle cx="990" cy="500" r="32" fill="var(--rim)"/>
    </svg>

    <p class="label tagline" style="left:222px; top:134px;"><span class="tagline__lead">1-DAY</span> GARAGE FLOOR APPLICATION</p>
    <span class="brand-mark" style="left:140px; top:180px; width:92px; height:100px;"></span>
    <p class="label brand-name brand-name--main" style="left:248px; top:188px;">MARROWIND</p>
    <p class="label brand-name brand-name--sub" style="left:248px; top:248px;">FLOOR COATINGS</p>
    <p class="label services services--band" style="left:128px; top:333px;">EPOXY FLOOR COATING INCLUDING LUXUXRY FLAKES<span class="divider">|</span>LUXURY METALLICS<span class="divider">|</span>LUXURY QUARTZ FOR OUTDOOR</p>
    <p class="label website" style="left:210px; top:369px;"><span class="website__name">WWW.MARROWINDFLOORCOATING</span><span class="website__tld">.COM</span></p>
    <p class="label phone" style="left:826px; top:353px;">555-014-2290</p>
  </section>

  <!-- Side B: black body with neon rear and floor photo circles -->
  <section class="van van--side-b" aria-label="Van wrap, version with green rear">
    <svg viewBox="0 0 1200 560" width="1200" height="560">
      <defs>
        <clipPath id="body-b">
          <path d="M80,125 Q80,98 112,98 L960,100 Q1008,102 1030,160 L1080,300 Q1140,318 1150,352 L1150,470 Q1150,492 1128,492 L80,495 Q68,495 68,480 Z"/>
        </clipPath>
      </defs>
      <g clip-path="url(#body-b)">
        <rect class="body-black" x="0" y="0" width="1200" height="560" fill="var(--black)"/>
        <path class="rear-panel" d="M0,90 L200,90 Q260,200 250,300 L290,420 L290,560 L0,560 Z" fill="var(--neon)"/>
        <rect class="rocker" x="70" y="440" width="1100" height="60" fill="#0a0a0a"/>
        <path class="front-window" d="M795,190 L920,190 Q945,192 955,240 L962,294 L795,294 Z" fill="var(--glass)"/>
        <rect class="headlight" x="1100" y="345" width="50" height="18" rx="6" fill="#d9dcdf"/>
      </g>
      <circle role="img" aria-label="Photo of a finished garage floor" cx="192" cy="160" r="46" fill="var(--floor-gray)" stroke="var(--black)" stroke-width="4"/>
      <circle role="img" aria-label="Photo of a flake epoxy floor close-up" cx="192" cy="255" r="46" fill="#b9bbbd" stroke="var(--black)" stroke-width="4"/>
      <circle role="img" aria-label="Photo of a coated garage interior" cx="248" cy="345" r="46" fill="#7e8184" stroke="var(--black)" stroke-width="4"/>
      <rect class="belt-line" x="300" y="292" width="270" height="5" fill="var(--white)"/>
      <rect class="website-band" x="292" y="326" width="433" height="25" fill="var(--white)"/>
      <rect class="phone-band" x="792" y="326" width="358" height="28" fill="var(--white)"/>
      <g class="warranty-seal">
        <circle cx="838" cy="403" r="30" fill="var(--charcoal)"/>
        <circle cx="838" cy="403" r="24" fill="none" stroke="var(--white)" stroke-width="2"/>
        <rect x="806" y="394" width="64" height="18" fill="var(--white)"/>
        <text class="seal-text" x="838" y="408" text-anchor="middle" font-size="12" fill="var(--black)">LIFETIME</text>
        <text class="seal-text" x="838" y="389" text-anchor="middle" font-size="6.5" fill="var(--white)">WARRANTY</text>
        <text class="seal-text" x="838" y="423" text-anchor="middle" font-size="6.5" fill="var(--white)">WARRANTY</text>
      </g>
      <circle class="wheel" cx="255" cy="500" r="55" fill="var(--tire)"/>
      <circle cx="255" cy="500" r="32" fill="var(--rim)"/>
      <circle class="wheel" cx="990" cy="500" r="55" fill="var(--tire)"/>
      <circle cx="990" cy="500" r="32" fill="var(--rim)"/>
    </svg>

    <p class="label tagline" style="left:352px; top:122px;"><span class="tagline__lead">1-DAY</span> GARAGE FLOOR APPLICATION</p>
    <span class="brand-mark" style="left:275px; top:160px; width:92px; height:100px;"></span>
    <p class="label brand-name brand-name--main" style="left:385px; top:170px;">MARROWIND</p>
    <p class="label brand-name brand-name--sub" style="left:385px; top:232px;">FLOOR COATINGS</p>
    <p class="label website website--band" style="left:344px; top:331px;"><span class="website__name">WWW.MARROWINDFLOORCOATING</span><span class="website__tld">.COM</span></p>
    <p class="label phone" style="left:826px; top:329px;">555-014-2290</p>
    <p class="label services services--open" style="left:300px; top:381px; width:420px;">EPOXY FLOOR COATING INCLUDING LUXUXRY FLAKES<span class="divider">|</span>LUXURY METALLICS<br>LUXURY QUARTZ FOR OUTDOOR</p>
  </section>

</main>
</body>
</html>
```